Startup that helps high growth companies expand to new office locations needs a polished website

Hello! We are a B2B startup helping fast growing companies expand to new office locations. We are in need of a polished, vibrant website that is modern and professional. Our mission is to accelerate tech-enabled economic opportunity beyond silicon valley.
- Our current site is: https://www.pellanworks.co
- We help companies in 3 steps: Discover, Expand, Align
- Discover = analysis on where a company should expand to
geographically
- Expand = manage the entire office build out process
- Align = ongoing support at the new office and help culturally aligning
new office to HQ
- Look through our deck which is attached in this brief and incorporate parts of our deck into the website, especially content and messaging! Slide 2 in particular is important, so I've taken a screenshot of it individually and attached it.
- Please also carefully read through our branding document which includes color palettes and examples of websites we like. However, we are open to any ideas you think are better in terms of color and font! https://slides.marnotech.io/deck/7Qz_K2pLwRt9XyVbN4cHsJ8dFmA3eUoGi5/view#page=n8k2m4q7_0_0
- We need a strong call to action for customers to contact us

We are also looking for a new logo! This logo should convey that we help companies expand beyond their current office locations.

Thanks! Looking forward to seeing your designs!

Target Market(s)

hypergrowth startups of 100-500 people

Logo Text

PellanWorks

Coding

Coded - Design and coding required

Number of Pages Required

2 page

Font styles to use
Sans Serif

Requirements
Must have
• - Clear call to action on landing page
• - A separate about us page. Please refer to the wireframe attached
• - Incorporate content from the current homepage at https://www.pellanworks.co/ (Discover, Expand, Align content, which are the 3 pieces of our offering)
• - Incorporate messaging in Slide 2 of attached company ppt. I've also taken a screenshot of it individually and attached it.
• - Testimonials sections on homepage
Nice to have
• - Incorporate other elements of the slide deck as you see fit

```html
<!DOCTYPE html>
<html lang="en">
<head>
<meta charset="utf-8">
<title>PellanWorks — Distributed teams are the future of work</title>
<link href="https://fonts.googleapis.com/css2?family=Montserrat:wght@400;500;600;700;800&family=Open+Sans:wght@400;600&display=swap" rel="stylesheet">
<style>
:root{
  --navy:#1d3d5c;
  --navy-deep:#173250;
  --teal:#3bb9c9;
  --teal-dark:#2a8f9e;
  --ink:#2b3440;
  --muted:#7a8491;
  --line:#d9dde3;
  --lavender:#e9ebf6;
  --grey-band:#efeff1;
  --art-light:#e3e8f6;
  --art-mid:#b9c6ea;
  --art-deep:#6f86c9;
  --white:#ffffff;
}
*{box-sizing:border-box;margin:0;padding:0}
html,body{width:1200px;height:4944px;overflow:hidden}
body{font-family:"Open Sans",Arial,sans-serif;color:var(--ink);background:var(--white);position:relative}
h1,h2,h3,h4,.brand,.nav a,.btn{font-family:"Montserrat",Arial,sans-serif}
section,header,footer{position:absolute;left:0;width:1200px}
.btn{display:inline-block;font-size:12px;font-weight:600;letter-spacing:1.5px;text-transform:uppercase;padding:14px 28px;text-decoration:none}

/* header + hero */
.hero{top:0;height:460px;background:linear-gradient(180deg,#6d8aa3 0%,#3c5d7d 45%,#1e3f60 100%)}
.hero .photo{position:absolute;inset:72px 0 0 0;background:linear-gradient(180deg,rgba(140,170,195,.35),rgba(25,60,95,.6))}
.topbar{position:absolute;top:0;left:0;width:1200px;height:72px;background:var(--white);display:flex;align-items:center;justify-content:space-between;padding:0 40px 0 150px}
.brand{display:flex;align-items:center;gap:10px;font-size:24px;font-weight:800;color:var(--navy)}
.brand .dot{width:14px;height:14px;border-radius:50%;background:var(--teal)}
.nav{display:flex;gap:36px}
.nav a{font-size:13px;color:var(--ink);text-decoration:none;padding-bottom:6px}
.nav a.active{border-bottom:2px solid var(--teal)}
.hero-copy{position:absolute;top:190px;width:1200px;text-align:center;color:var(--white)}
.hero-copy .lead{font-family:"Montserrat",sans-serif;font-size:34px;font-weight:500}
.hero-copy h1{font-size:66px;font-weight:800;letter-spacing:2px;line-height:1.1;margin-top:4px}
.hero-copy h1 span{color:var(--teal)}
.hero-copy p{font-size:18px;margin-top:6px}
.hero-copy .btn{margin-top:26px;border:2px solid var(--white);color:var(--white)}

/* about */
.about{top:540px;height:500px}
.icon-badge{width:30px;height:30px}
.about .copy{position:absolute;left:150px;top:120px;width:300px}
.section-title{font-size:26px;font-weight:700;letter-spacing:2px;color:var(--ink);margin:14px 0 22px}
.body-text{font-size:13px;line-height:1.75;color:var(--muted)}
.body-text+.body-text{margin-top:18px}
.read-more{display:inline-flex;align-items:center;gap:10px;margin-top:30px;font-size:12px;font-weight:600;color:var(--navy);text-transform:uppercase;letter-spacing:1px;text-decoration:none}
.about .map-title{position:absolute;left:750px;top:92px;font-family:"Montserrat",sans-serif;font-size:22px;font-weight:600;color:var(--navy)}
.about .map{position:absolute;left:600px;top:135px;width:570px;height:340px;background:linear-gradient(135deg,#e9edf3,#d3dbe6);border-radius:6px}

/* slide 2 message */
.help{top:1112px;height:588px;background:var(--lavender)}
.help .illustration{position:absolute;left:0;top:0;width:520px;height:588px;background:linear-gradient(160deg,#f3f1ec 0%,#d9d4c8 55%,#c7cfdc 100%)}
.help .brand{position:absolute;left:575px;top:90px;font-size:30px}
.help .tag{position:absolute;left:578px;top:130px;font-size:11px;color:var(--muted)}
.checklist{position:absolute;left:580px;top:190px;list-style:none;width:520px}
.checklist li{display:flex;gap:14px;align-items:flex-start;font-size:17px;font-weight:600;color:var(--navy);margin-bottom:22px;line-height:1.4}
.checklist li u{color:var(--teal-dark)}
.checklist svg{flex:none;margin-top:2px}
.help h2{position:absolute;left:690px;top:468px;font-size:52px;font-weight:800;color:var(--navy);letter-spacing:1px}
.help .note{position:absolute;left:760px;top:530px;font-size:11px;color:var(--muted)}

/* steps */
.steps{top:1700px;height:1420px}
.steps .curve{position:absolute;left:0;top:0}
.step{position:absolute;width:330px}
.step h3{font-size:26px;font-weight:700;letter-spacing:2px;margin:14px 0 16px}
.step-art{position:absolute;border-radius:14px;background:radial-gradient(ellipse at 50% 60%,var(--art-mid) 0%,var(--art-light) 55%,rgba(255,255,255,0) 80%)}
.step-art.network{background:radial-gradient(ellipse at 50% 55%,#c6d3f2 0%,#e6ecf9 50%,rgba(255,255,255,0) 78%)}
.step-art.meeting{background:linear-gradient(160deg,#eef1fa 0%,#c3cff0 55%,#8fa3dc 100%)}
.step-art.office{background:linear-gradient(160deg,#e8edf9 0%,#b6c4ec 50%,var(--art-deep) 100%)}
.discover{left:150px;top:112px}
.expand{left:680px;top:620px}
.align{left:150px;top:1010px}

/* blog */
.blog{top:3160px;height:560px}
.blog h2{text-align:center;font-size:22px;font-weight:700;letter-spacing:2px;margin-top:28px}
.cards{position:absolute;top:100px;left:200px;display:flex;gap:40px}
.card{width:240px}
.card .thumb{height:168px;background:linear-gradient(180deg,#7e96b0,#324d68);position:relative}
.card .thumb .date{position:absolute;left:0;bottom:0;width:46px;height:46px;background:var(--navy);color:var(--white);font-size:11px;text-align:center;padding-top:8px;line-height:1.3}
.meta{display:flex;justify-content:space-between;align-items:center;font-size:11px;color:var(--muted);margin:14px 0 10px}
.meta .author{display:flex;align-items:center;gap:6px}
.meta .avatar{width:20px;height:20px;border-radius:50%;background:var(--line)}
.card h4{font-size:12px;font-weight:700;color:var(--teal-dark);line-height:1.5;text-transform:uppercase}
.card p{font-size:11.5px;line-height:1.65;color:var(--muted);margin-top:8px}
.blog .btn{position:absolute;left:500px;top:460px;background:var(--navy);color:var(--white)}

/* testimonials */
.testimonials{top:3760px;height:360px;background:var(--grey-band)}
.testimonials .bubble{position:absolute;left:440px;top:-28px}
.testimonials .heading{position:absolute;left:150px;top:120px}
.testimonials .heading .small{font-family:"Montserrat",sans-serif;font-size:20px;font-weight:500;letter-spacing:2px}
.testimonials h2{font-size:38px;font-weight:700;letter-spacing:2px;line-height:1.1}
.faces{position:absolute;left:230px;top:250px;display:flex;gap:10px;align-items:center}
.faces .face{width:34px;height:34px;border-radius:50%;background:#c9cdd4;border:2px solid var(--white)}
.faces .face.on{background:var(--teal)}
.faces .arrow{color:var(--muted);font-size:16px}
.testimonials .rule{position:absolute;left:580px;top:95px;width:1px;height:190px;background:var(--line)}
.quote{position:absolute;left:620px;top:130px;width:380px}
.quote .mark{font-family:Georgia,serif;font-size:40px;color:var(--line);position:absolute;left:-30px;top:-30px}
.quote p{font-size:13.5px;line-height:1.75;color:var(--muted)}
.quote .who{margin-top:14px;font-size:11px;font-weight:700;color:var(--navy);letter-spacing:1px}

/* contact */
.contact{top:4180px;height:460px;text-align:center}
.contact h2{font-size:22px;font-weight:700;letter-spacing:3px;margin-top:20px}
.contact .sub{font-size:12px;color:var(--muted);margin-top:6px}
.form{position:absolute;left:430px;top:110px;width:340px;text-align:left}
.row{display:flex;gap:20px}
.field{flex:1;border-bottom:1px solid var(--line);font-size:11px;color:var(--muted);padding:10px 0 8px;margin-bottom:14px}
.field.tall{height:110px}
.form .btn{margin-top:22px;margin-left:70px;background:var(--navy);color:var(--white);padding:12px 34px}

/* footer */
.footer{top:4688px;height:256px;background:var(--navy-deep);color:var(--white);text-align:center}
.footer .brand{justify-content:center;color:var(--white);margin-top:48px;font-size:24px}
.footer .tag{font-size:10px;color:#9fb0c2;margin-top:4px}
.social{display:flex;justify-content:center;gap:18px;margin-top:30px}
.social span{width:12px;height:12px;border-radius:50%;background:#9fb0c2}
.footer .links{display:flex;justify-content:center;gap:26px;margin-top:22px;font-size:11px;color:#c8d3de}
.footer .legal{font-size:10px;color:#8797a8;margin-top:12px}
</style>
</head>
<body>

<header class="hero">
  <div class="photo" role="img" aria-label="City skyline photograph in blue tones"></div>
  <div class="topbar">
    <div class="brand"><span>PellanWorks</span><span class="dot"></span></div>
    <nav class="nav">
      <a class="active" href="#">Home</a><a href="#">Offering</a><a href="#">About Us</a><a href="#">Blog</a><a href="#">Contact Us</a>
    </nav>
  </div>
  <div class="hero-copy">
    <div class="lead">Distributed teams are the future of work.</div>
    <h1>ARE YOU <span>READY?</span></h1>
    <p>We are your turnkey solution to grow beyond Silicon Valley</p>
    <a class="btn" href="#">Contact Us</a>
  </div>
</header>

<section class="about">
  <div class="copy">
    <svg class="icon-badge" viewBox="0 0 30 30"><rect x="4" y="8" width="22" height="18" fill="none" stroke="#1d3d5c" stroke-width="2"/><path d="M10 8V4h10v4M4 15h22" stroke="#1d3d5c" stroke-width="2" fill="none"/></svg>
    <h2 class="section-title">ABOUT US</h2>
    <p class="body-text">We help fast growing teams open new offices beyond the Valley. From choosing the right city to hiring locally and setting up the space, we guide every step so your team can keep shipping while you grow.</p>
    <p class="body-text">Our mission is to bring tech-enabled economic opportunity to new cities.</p>
    <a class="read-more" href="#">Read more <svg width="20" height="10" viewBox="0 0 20 10"><path d="M0 5h18M14 1l4 4-4 4" stroke="#1d3d5c" stroke-width="1.5" fill="none"/></svg></a>
  </div>
  <div class="map-title">Where will your next office be?</div>
  <div class="map" role="img" aria-label="Map of the United States with pins marking candidate office cities"></div>
</section>

<section class="help">
  <div class="illustration" role="img" aria-label="Illustration of a house under construction on blueprints with small workers"></div>
  <div class="brand"><span>PellanWorks</span><span class="dot"></span></div>
  <div class="tag">Turnkey solution for high growth companies</div>
  <ul class="checklist">
    <li><svg width="20" height="20" viewBox="0 0 20 20"><circle cx="10" cy="10" r="10" fill="#3bb9c9"/><path d="M5 10l3.5 3.5L15 7" stroke="#fff" stroke-width="2" fill="none"/></svg><span>Are you paying top dollar and <u>still losing talent?</u></span></li>
    <li><svg width="20" height="20" viewBox="0 0 20 20"><circle cx="10" cy="10" r="10" fill="#3bb9c9"/><path d="M5 10l3.5 3.5L15 7" stroke="#fff" stroke-width="2" fill="none"/></svg><span>Are you built funded and still <u>not able to hire fast enough?</u></span></li>
    <li><svg width="20" height="20" viewBox="0 0 20 20"><circle cx="10" cy="10" r="10" fill="#3bb9c9"/><path d="M5 10l3.5 3.5L15 7" stroke="#fff" stroke-width="2" fill="none"/></svg><span>Are you able to <u>quickly scale</u> remote offices?</span></li>
    <li><svg width="20" height="20" viewBox="0 0 20 20"><circle cx="10" cy="10" r="10" fill="#3bb9c9"/><path d="M5 10l3.5 3.5L15 7" stroke="#fff" stroke-width="2" fill="none"/></svg><span>Are you getting <u>the right support</u> from your local relationships/government/leaders?</span></li>
    <li><svg width="20" height="20" viewBox="0 0 20 20"><circle cx="10" cy="10" r="10" fill="#3bb9c9"/><path d="M5 10l3.5 3.5L15 7" stroke="#fff" stroke-width="2" fill="none"/></svg><span>Are you <u>paying too much for everything?</u></span></li>
  </ul>
  <h2>WE CAN HELP.</h2>
  <div class="note">*Talent = Headcount is 80% of Costs</div>
</section>

<section class="steps">
  <svg class="curve" width="1200" height="1420" viewBox="0 0 1200 1420">
    <path d="M0 40 C300 0 420 260 260 520 C140 720 0 700 0 700Z" fill="#f3f4f6"/>
    <path d="M1200 520 C1020 600 1000 900 1200 980Z" fill="#f3f4f6"/>
  </svg>

  <div class="step discover">
    <svg class="icon-badge" viewBox="0 0 30 30"><circle cx="15" cy="15" r="11" fill="none" stroke="#1d3d5c" stroke-width="2"/><circle cx="15" cy="15" r="4" fill="#1d3d5c"/></svg>
    <h3>DISCOVER</h3>
    <p class="body-text">We help you identify and evaluate the best cities and talent to grow your team. From labor availability to cost of living, we weigh all the key factors you need to make a decision.</p>
  </div>
  <div class="step-art network" style="left:560px;top:110px;width:560px;height:340px" role="img" aria-label="Illustration of a connected network of team members"></div>

  <div class="step-art meeting" style="left:120px;top:560px;width:500px;height:340px" role="img" aria-label="Illustration of a team meeting around a table with charts"></div>
  <div class="step expand">
    <svg class="icon-badge" viewBox="0 0 30 30"><path d="M15 3v24M3 15h24M15 3l-4 4M15 3l4 4M15 27l-4-4M15 27l4-4M3 15l4-4M3 15l4 4M27 15l-4-4M27 15l-4 4" stroke="#1d3d5c" stroke-width="2" fill="none"/></svg>
    <h3>EXPAND</h3>
    <p class="body-text">We set up your expansion end to end. Hiring an operational leader and team, leasing the right space, legal and tax setup, IT and furniture, and managing every vendor for you.</p>
  </div>

  <div class="step align">
    <svg class="icon-badge" viewBox="0 0 30 30"><path d="M4 8h22M4 15h22M4 22h22" stroke="#1d3d5c" stroke-width="2"/></svg>
    <h3>ALIGN</h3>
    <p class="body-text">We stay on as ongoing support. Culture, events, recruiting and office operations keep your new site aligned with HQ as it grows.</p>
  </div>
  <div class="step-art office" style="left:600px;top:1010px;width:560px;height:350px" role="img" aria-label="Illustration of a team working together in an office with dashboards"></div>
</section>

<section class="blog">
  <h2>LATEST IN BLOG</h2>
  <div class="cards">
    <article class="card">
      <div class="thumb" role="img" aria-label="City photograph"><div class="date">12<br>Jun</div></div>
      <div class="meta"><span class="author"><span class="avatar"></span>Lena Ortiz</span><span>♡ 4 · 2</span></div>
      <h4>Choosing your second office city in 2019</h4>
      <p>What to weigh when you plan a new site, from talent pools to rent, taxes and travel time.</p>
    </article>
    <article class="card">
      <div class="thumb" role="img" aria-label="City photograph"><div class="date">08<br>Jun</div></div>
      <div class="meta"><span class="author"><span class="avatar"></span>Lena Ortiz</span><span>♡ 4 · 2</span></div>
      <h4>Building culture across distributed teams</h4>
      <p>Simple habits that keep remote offices connected to HQ and moving in the same direction.</p>
    </article>
    <article class="card">
      <div class="thumb" role="img" aria-label="City photograph"><div class="date">02<br>Jun</div></div>
      <div class="meta"><span class="author"><span class="avatar"></span>Lena Ortiz</span><span>♡ 4 · 2</span></div>
      <h4>Hiring fast in a new market without mistakes</h4>
      <p>How to find a local leader, partner with schools and fill roles in weeks instead of months.</p>
    </article>
  </div>
  <a class="btn" href="#">View more blog</a>
</section>

<section class="testimonials">
  <svg class="bubble" width="70" height="40" viewBox="0 0 70 40"><path d="M0 40 C10 10 40 0 70 0 C60 20 50 30 40 40Z" fill="#1d3d5c"/></svg>
  <div class="heading">
    <div class="small">WHAT OUR</div>
    <h2>CUSTOMER &nbsp;SAYS</h2>
  </div>
  <div class="faces">
    <span class="face"></span><span class="face on"></span><span class="face"></span><span class="face"></span>
    <span class="arrow">‹ ›</span>
  </div>
  <div class="rule"></div>
  <div class="quote">
    <span class="mark">“</span>
    <p>They found our new city, hired our site lead and had the office running in under three months. Our new team feels every bit as connected as HQ, and our costs dropped.</p>
    <div class="who">MAREN HOLT</div>
  </div>
</section>

<section class="contact">
  <h2>GET IN TOUCH</h2>
  <div class="sub">Any questions or remarks? Just write us a message!</div>
  <div class="form">
    <div class="row"><div class="field">First Name</div><div class="field">Phone Number</div></div>
    <div class="field">Email Address</div>
    <div class="field">Subject</div>
    <div class="field tall">Message</div>
    <a class="btn" href="#">Submit Now</a>
  </div>
</section>

<footer class="footer">
  <div class="brand"><span>PellanWorks</span><span class="dot"></span></div>
  <div class="tag">Turnkey solution for high growth companies</div>
  <div class="social"><span></span><span></span><span></span><span></span></div>
  <div class="links"><span>Home</span><span>Offering</span><span>About Us</span><span>Blog</span><span>Contact Us</span></div>
  <div class="legal">© 2019 PellanWorks. All rights reserved. · Terms &amp; Conditions · Privacy Policy</div>
</footer>

</body>
</html>
```